Branvique needs a business Card Design

We are looking for a business card Design for our new Managed Service Provider Company, Branvique. Branvique encompasses everything IT for the average medium sized business. Our primary services are help desk support, cyber-security (malware and ransomware protection), and Disaster Recovery systems. We would like the design to have a very clean and professional look, with a very minimalist feel.

Target Market(s)

Medium to large sized businesses

Industry/Entity Type

It Service

Contact Information for Business Card

Name GoesHere
name@branvique.com
O: 555-382-6047
C: 555-731-5820

Font styles to use
Other font styles liked:
• Poppins Font Only Please

Colors

Designer to choose only greyscale colors for use in the design.

Requirements
Must have
• Logo included
Nice to have
• Cutting Edge, innovative, minimalistic, elegant

```html
<!DOCTYPE html>
<html lang="en">
<head>
<meta charset="UTF-8">
<title>Branvique Business Card</title>
<link href="https://fonts.googleapis.com/css2?family=Poppins:wght@400;600&display=swap" rel="stylesheet">
<style>
  :root {
    --charcoal: #222222;
    --charcoal-soft: #2c2c2c;
    --paper: #ffffff;
    --ink: #333333;
    --stage: #d9d9d9;
    --shadow: rgba(0, 0, 0, 0.35);
  }
  * { margin: 0; padding: 0; box-sizing: border-box; }
  html, body {
    width: 1200px;
    height: 802px;
    overflow: hidden;
    background: var(--stage);
    font-family: "Poppins", sans-serif;
  }
  .canvas { position: relative; width: 1200px; height: 802px; }
  .card {
    position: absolute;
    top: 274px;
    width: 443px;
    height: 264px;
    box-shadow: 2px 3px 6px var(--shadow);
    overflow: hidden;
  }
  .card-front { left: 136px; background: var(--paper); }
  .card-back { left: 624px; background: var(--charcoal); }

  .side-band {
    position: absolute; left: 0; top: 0;
    width: 40px; height: 100%;
    background: var(--charcoal);
  }
  .side-rule {
    position: absolute; left: 42px; top: 0;
    width: 3px; height: 100%;
    background: var(--charcoal);
  }

  .wordmark {
    position: absolute;
    right: 37px;
    top: 106px;
    font-size: 16px;
    font-weight: 400;
    letter-spacing: 7px;
    margin-right: -7px;
    color: var(--charcoal);
    display: flex;
    align-items: center;
    gap: 9px;
    line-height: 20px;
  }
  .wordmark-mark {
    width: 11px; height: 11px;
    background: var(--charcoal);
  }

  .person { position: absolute; left: 69px; top: 140px; }
  .person-name {
    font-size: 16px; font-weight: 600;
    color: var(--charcoal); line-height: 1.05;
  }
  .person-title {
    font-size: 12.5px; font-weight: 400;
    color: var(--ink); line-height: 1.2;
  }

  .contact-list {
    position: absolute; left: 69px; top: 188px;
    list-style: none;
  }
  .contact-item {
    display: flex; align-items: center; gap: 6px;
    font-size: 12.5px; color: var(--ink);
    height: 16px;
  }
  .contact-icon { width: 10px; height: 10px; fill: var(--charcoal); flex: none; }

  .back-field {
    position: absolute; inset: 0;
    background: linear-gradient(135deg, var(--charcoal-soft) 0%, var(--charcoal) 55%, var(--charcoal-soft) 100%);
  }
  .back-wordmark {
    position: absolute;
    left: 0; right: 0; top: 50%;
    transform: translateY(-50%);
    text-align: center;
    font-size: 16px;
    letter-spacing: 7px;
    text-indent: 7px;
    color: var(--paper);
  }
</style>
</head>
<body>
<main class="canvas">
  <section class="card card-front">
    <div class="side-band"></div>
    <div class="side-rule"></div>

    <div class="wordmark"><span class="wordmark-mark"></span>BRANVIQUE</div>

    <div class="person">
      <p class="person-name">MARCUS HALE</p>
      <p class="person-title">Managing Director</p>
    </div>

    <ul class="contact-list">
      <li class="contact-item">
        <svg class="contact-icon" viewBox="0 0 10 10"><path d="M1 3 Q5 0 9 3 L8 4.5 L6.5 3.8 L6.5 3 Q5 2.6 3.5 3 L3.5 3.8 L2 4.5 Z M2.5 5 H7.5 L8.5 9 H1.5 Z"/></svg>
        <span>555-382-6047</span>
      </li>
      <li class="contact-item">
        <svg class="contact-icon" viewBox="0 0 10 10"><path d="M3 0.5 H7 Q7.8 0.5 7.8 1.3 V8.7 Q7.8 9.5 7 9.5 H3 Q2.2 9.5 2.2 8.7 V1.3 Q2.2 0.5 3 0.5 Z M3.1 1.6 V7.6 H6.9 V1.6 Z" fill-rule="evenodd"/></svg>
        <span>555-731-5820</span>
      </li>
      <li class="contact-item">
        <svg class="contact-icon" viewBox="0 0 10 10"><path d="M0.5 2 H9.5 V8 H0.5 Z M1.2 2.6 L5 5.6 L8.8 2.6 V7.4 H1.2 Z" fill-rule="evenodd"/></svg>
        <span>name@branvique.com</span>
      </li>
    </ul>
  </section>

  <section class="card card-back">
    <div class="back-field" role="img" aria-label="Faint tonal repeat pattern across the dark grey back"></div>
    <div class="back-wordmark">BRANVIQUE</div>
  </section>
</main>
</body>
</html>
```